Corporate Business Card

Very professional, Modern, Not to busy, include phone address email, website
(555) 555-0174, 61807 19th Street N, Alder Falls, WA 98517, marcus@kestrelbayholding.com, brelvanindustries.com

Target Market(s)

Manufacturing

Industry/Entity Type

Aero, machining, manufacturing, Off road racing

Contact Information for Business Card

Phone, address email, website

```html
<!DOCTYPE html>
<html lang="en">
<head>
<meta charset="utf-8">
<title>Brelvan Industries – Business Card</title>
<link href="https://fonts.googleapis.com/css2?family=Montserrat:wght@400;500;700&display=swap" rel="stylesheet">
<style>
  :root {
    --stage: #6c6c6c;
    --navy: #15336b;
    --red: #d0222a;
    --ink: #141414;
    --paper: #ffffff;
  }
  * { margin: 0; padding: 0; box-sizing: border-box; }
  html, body { width: 1200px; height: 801px; overflow: hidden; }
  body {
    background: var(--stage);
    font-family: "Montserrat", sans-serif;
    position: relative;
  }
  .card {
    position: absolute;
    top: 252px;
    width: 520px;
    height: 297px;
    overflow: hidden;
    box-shadow: 0 14px 30px rgba(0,0,0,.35);
    border-bottom: 2px solid var(--red);
  }
  .card--front { left: 50px; background: var(--paper); }
  .card--back { left: 630px; background: var(--navy); }
  .card__art { position: absolute; inset: 0; }

  .wordmark {
    position: absolute;
    font-weight: 700;
    line-height: 1;
    letter-spacing: .02em;
  }
  .card--front .wordmark {
    left: 190px; top: 30px;
    color: var(--navy);
    font-size: 34px;
  }
  .card--front .wordmark small {
    display: block;
    font-size: 15px;
    margin-top: 4px;
    text-align: right;
    letter-spacing: .04em;
  }
  .card--back .wordmark {
    left: 0; right: 0; top: 98px;
    text-align: center;
    color: var(--paper);
    font-size: 62px;
  }
  .card--back .wordmark small {
    display: block;
    font-size: 26px;
    margin-top: 8px;
    letter-spacing: .05em;
  }

  .holder { position: absolute; left: 30px; top: 176px; }
  .holder__name {
    color: var(--red);
    font-weight: 700;
    font-size: 19px;
    letter-spacing: .02em;
    text-transform: uppercase;
  }
  .holder__role { color: var(--paper); font-size: 12px; margin-top: 2px; }

  .contacts { position: absolute; left: 30px; top: 228px; list-style: none; }
  .contacts li {
    display: flex; align-items: center; gap: 8px;
    color: var(--paper); font-size: 11.5px; height: 19px;
  }
  .contacts svg { width: 11px; height: 11px; fill: var(--red); flex: none; }

  .address {
    position: absolute; right: 24px; top: 140px;
    color: var(--paper); font-size: 12px; line-height: 1.5;
    text-align: right; font-style: normal;
  }
</style>
</head>
<body>

<section class="card card--front" aria-label="Business card front">
  <svg class="card__art" viewBox="0 0 520 297" aria-hidden="true">
    <path d="M0 60 C140 150 330 130 520 20 L520 297 L0 297 Z" fill="var(--red)"/>
    <path d="M0 65 C140 155 330 135 520 25 L520 297 L0 297 Z" fill="var(--paper)"/>
    <path d="M0 69 C140 159 330 139 520 29 L520 297 L0 297 Z" fill="var(--navy)"/>
    <path d="M0 79 C140 169 330 149 520 39 L520 297 L0 297 Z" fill="var(--paper)"/>
    <path d="M0 82 C140 172 330 152 520 42 L520 297 L0 297 Z" fill="var(--ink)"/>
  </svg>

  <div class="wordmark">BRELVAN<small>Industries</small></div>

  <address class="address">61807 19th Street N<br>Alder Falls, WA 98517</address>

  <div class="holder">
    <p class="holder__name">Daniel Corwin</p>
    <p class="holder__role">Owner/CEO</p>
  </div>

  <ul class="contacts">
    <li><svg viewBox="0 0 24 24"><path d="M6.6 10.8a15.1 15.1 0 0 0 6.6 6.6l2.2-2.2a1 1 0 0 1 1-.25 11.4 11.4 0 0 0 3.6.57 1 1 0 0 1 1 1V20a1 1 0 0 1-1 1A17 17 0 0 1 3 4a1 1 0 0 1 1-1h3.5a1 1 0 0 1 1 1c0 1.25.2 2.45.57 3.57a1 1 0 0 1-.25 1z"/></svg>(555) 555-0174</li>
    <li><svg viewBox="0 0 24 24"><path d="M2 5h20v14H2z M2 5l10 8 10-8" /></svg>marcus@kestrelbayholding.com</li>
    <li><svg viewBox="0 0 24 24"><circle cx="12" cy="12" r="10"/></svg>www.brelvanindustries.com</li>
  </ul>
</section>

<section class="card card--back" aria-label="Business card back">
  <div class="wordmark">BRELVAN<small>Industries</small></div>
</section>

</body>
</html>
```